Security based company delivering High Risk Training to Law Enforcement Agencies Worldwide.

We need a Web design for a company doing business in Washington D.C. We deliver High Risk Training to Law Enforcement Agencies throughout the world. Our focus is on Improvised Explosive Devices. We train Bomb Technicians and First Responders in all aspects relating to bombings and criminal incidents globally.

Reason: We have uploaded our logo. Thank you.

Target Market(s)

Military and Law Enforcement Personnel from around the world.

Industry/Entity Type

Business

Requirements
Should not have
• Do not include cartoon like characters.

```html
<!DOCTYPE html>
<html lang="en">
<head>
<meta charset="utf-8">
<title>Ordnance Response Group</title>
<link href="https://fonts.googleapis.com/css2?family=Gelasio&family=PT+Sans+Narrow:wght@400;700&family=Cabin:wght@400;500&family=Open+Sans:wght@300;400&display=swap" rel="stylesheet">
<style>
:root{
  --navy:#112d4f;
  --ink:#1d3a55;
  --grey:#6f7479;
  --btn-top:#c3dde7;
  --btn-bot:#8fb6c6;
  --footer:#3a5563;
  --link-yellow:#e9d335;
  --white:#ffffff;
  --hero-sky:#9a9fae;
  --hero-ground:#c9b08a;
}
*{margin:0;padding:0;box-sizing:border-box}
html,body{width:955px;height:1200px;overflow:hidden;background:var(--white)}
body{position:relative;font-family:"Cabin",sans-serif;color:var(--ink)}
.abs{position:absolute}

/* header */
.brand{left:108px;top:18px;font-family:"Gelasio",serif;font-size:29px;line-height:33px;color:#1f3140}
.brand .line2{display:block;padding-left:67px}
.top-icons{left:742px;top:10px;display:flex;gap:11px}
.top-icons span{width:25px;height:25px;border-radius:3px;display:block}
.sq-blue{background:linear-gradient(#6b8fd6,#3a5fae)}
.sq-teal{background:linear-gradient(#7fd0e6,#3ba3c4)}
.sq-grey{background:linear-gradient(#e6e6e6,#b8b8b8);display:flex!important;align-items:center;justify-content:center}
.nav{left:496px;top:53px;display:flex;gap:0;font-size:13px}
.nav a{color:var(--ink);text-decoration:none;height:30px;line-height:30px;padding:0 12.5px}
.nav a.active{background:linear-gradient(var(--btn-top),var(--btn-bot));padding:0 13px}

/* hero */
.hero{left:0;top:96px;width:955px;height:427px;background:linear-gradient(180deg,var(--hero-sky) 0%,#c4c1bb 40%,#d9cdb8 70%,var(--hero-ground) 100%)}
.hero-caption{left:202px;top:310px;width:551px;height:55px;background:rgba(255,255,255,.82);font-family:"Cabin",sans-serif;font-size:24px;color:var(--navy);text-align:center;line-height:55px;letter-spacing:.2px}
.arrow{top:307px;width:38px;height:40px;background:rgba(60,60,60,.8);display:flex;align-items:center;justify-content:center}

/* content */
.h-title{left:0;width:955px;text-align:center;font-family:"PT Sans Narrow",sans-serif;font-weight:700;font-size:21px;color:var(--navy)}
.intro{left:108px;top:563px;width:740px;text-align:center;font-family:"Open Sans",sans-serif;font-weight:300;font-size:11px;line-height:19px;color:var(--grey)}
.btn{background:linear-gradient(var(--btn-top),var(--btn-bot));color:var(--ink);font-size:14px;text-align:center;box-shadow:0 2px 3px rgba(0,0,0,.2)}
.btn.corner::after{content:"";position:absolute;right:0;top:0;border-top:14px solid var(--navy);border-left:14px solid transparent}
.read-more{left:439px;top:632px;width:82px;height:32px;line-height:32px}

.card{top:731px;width:177px}
.card-photo{width:177px;height:125px;position:relative}
.card-photo .btn{position:absolute;top:83px;width:81px;height:32px;line-height:32px;font-size:13.5px}
.card h3{font-weight:500;font-size:12px;color:var(--navy);margin-top:7px}
.card p{font-family:"Open Sans",sans-serif;font-weight:300;font-size:10px;line-height:12.5px;color:var(--grey);margin-top:4px}
.card .quote{margin-top:8px;width:110px;height:29px;line-height:29px;font-size:13.5px;position:relative}

/* footer */
.footer{left:0;top:984px;width:955px;height:216px;background:var(--footer);color:var(--white)}
.footer h4{font-family:"Cabin",sans-serif;font-weight:400;font-size:15px}
.col{top:16px}
.quick a{display:block;color:var(--white);text-decoration:none;font-size:11px;margin-top:10px;line-height:14px}
.post h5{font-weight:400;font-size:13px;margin-top:6px}
.post p{font-family:"Open Sans",sans-serif;font-size:10.5px;line-height:13px;margin-top:5px;color:#e8eef1}
.post .url{color:var(--link-yellow);font-family:"Open Sans",sans-serif;font-size:10.5px;line-height:13px}
.follow{display:flex;gap:16px;margin-top:17px}
.follow span{width:24px;height:24px;border-radius:3px;display:block}
.sq-li{background:linear-gradient(#6f94d6,#3c62b0)}
.sq-or{background:linear-gradient(#f6a640,#e07a12)}
.copy{left:680px;top:178px;font-size:10px}
.code{left:878px;top:178px;font-size:10px}
</style>
</head>
<body>

<header>
  <div class="abs brand">Ordnance<span class="line2">Response Group</span></div>
  <div class="abs top-icons">
    <span class="sq-blue" role="img" aria-label="Social page"></span>
    <span class="sq-teal" role="img" aria-label="Social feed"></span>
    <span class="sq-grey" role="img" aria-label="Search">
      <svg width="14" height="14" viewBox="0 0 14 14"><circle cx="6" cy="6" r="4.2" fill="none" stroke="#555" stroke-width="1.6"/><line x1="9" y1="9" x2="12.5" y2="12.5" stroke="#555" stroke-width="1.8" stroke-linecap="round"/></svg>
    </span>
  </div>
  <nav class="abs nav">
    <a class="active" href="#">Home</a><a href="#">About</a><a href="#">Products</a><a href="#">Solutions</a><a href="#">Contact Us</a>
  </nav>
</header>

<section class="abs hero" role="img" aria-label="Bomb technician in protective suit approaching a device beside a stop sign and concrete barrier"></section>
<div class="abs hero-caption">LORIUM IPSUM UT ENIM AD MINIMA</div>
<div class="abs arrow" style="left:0"><svg width="12" height="18" viewBox="0 0 12 18"><path d="M9 2 3 9l6 7" fill="none" stroke="#fff" stroke-width="3"/></svg></div>
<div class="abs arrow" style="left:917px"><svg width="12" height="18" viewBox="0 0 12 18"><path d="M3 2l6 7-6 7" fill="none" stroke="#fff" stroke-width="3"/></svg></div>

<h1 class="abs h-title" style="top:530px">WELCOME</h1>
<p class="abs intro">Duis aute irure dolor in reprehenderit in voluptate velit esse cillum dolore eu fugiat nulla pariatur. Excepteur sint occaecat cupidatat non proident, sunt in culpa qui officia deserunt mollit anim id est laborum Sed ut perspiciatis unde omnis iste natus error sit voluptatem accusantium doloremque laudantium, totam rem aperiam, eaque ipsa quae ab illo inventore veritatis et quasi architecto.</p>
<div class="abs btn corner read-more">Read more</div>

<h2 class="abs h-title" style="top:690px">HIGH RISK TRAINING TO LAW ENFORCEMENT AGENCIES</h2>

<article class="abs card" style="left:102px">
  <div class="card-photo" role="img" aria-label="Car engulfed in a training explosion" style="background:linear-gradient(135deg,#c9b49a,#e3a04a 60%,#b9a58c)">
    <div class="btn corner" style="left:45px;top:83px">About Me</div>
  </div>
  <h3>Agency Name</h3>
  <p>Duis aute irure dolor in reprehenderit in voluptate velit esse cillum dolore eu fugiat nulla pariatur.</p>
  <div class="btn quote">Request a Quote</div>
</article>
<article class="abs card" style="left:294px">
  <div class="card-photo" role="img" aria-label="Car beside a blast with dark smoke" style="background:linear-gradient(135deg,#b9a996,#6b5a4e 55%,#c99a6a)">
    <div class="btn corner" style="left:48px;top:77px">About Me</div>
  </div>
  <h3>Agency Name</h3>
  <p>Duis aute irure dolor in reprehenderit in voluptate velit esse cillum dolore eu fugiat nulla pariatur.</p>
  <div class="btn quote">Request a Quote</div>
</article>
<article class="abs card" style="left:486px">
  <div class="card-photo" role="img" aria-label="Dust cloud rising from a desert test range" style="background:linear-gradient(180deg,#9ea1aa,#b7aa97 50%,#c2ad90)">
    <div class="btn corner" style="left:48px;top:77px">About Me</div>
  </div>
  <h3>Agency Name</h3>
  <p>Duis aute irure dolor in reprehenderit in voluptate velit esse cillum dolore eu fugiat nulla pariatur.</p>
  <div class="btn quote">Request a Quote</div>
</article>
<article class="abs card" style="left:677px">
  <div class="card-photo" role="img" aria-label="Debris thrown into the air by a controlled detonation" style="background:linear-gradient(180deg,#a7a8af,#8f8679 45%,#c1ab8c)">
    <div class="btn corner" style="left:48px;top:77px">About Me</div>
  </div>
  <h3>Agency Name</h3>
  <p>Duis aute irure dolor in reprehenderit in voluptate velit esse cillum dolore eu fugiat nulla pariatur.</p>
  <div class="btn quote">Request a Quote</div>
</article>

<footer class="abs footer">
  <div class="abs col quick" style="left:96px">
    <h4>Quick Links</h4>
    <a href="#" style="margin-top:14px">Home</a><a href="#">About us</a><a href="#">Products</a><a href="#">Contact Us</a>
  </div>
  <div class="abs col post" style="left:248px;width:180px">
    <h4>News</h4>
    <h5>Lorium</h5>
    <p>Lorem ipsum dolor sit amet, con-<br>sectetur adipisicing</p>
    <div class="url">http://fieldnote.net/4xPq7Lm</div>
    <h5 style="margin-top:12px">Lorium</h5>
    <p>Lorem ipsum dolor sit amet, con-<br>sectetur adipisicing</p>
    <div class="url">http://fieldnote.net/4xPq7Lm</div>
  </div>
  <div class="abs col post" style="left:449px;width:180px">
    <h4>Blog</h4>
    <h5>Lorium</h5>
    <p>Lorem ipsum dolor sit amet, con-<br>sectetur adipisicing</p>
    <div class="url">http://fieldnote.net/4xPq7Lm</div>
    <h5 style="margin-top:12px">Lorium</h5>
    <p>Lorem ipsum dolor sit amet, con-<br>sectetur adipisicing</p>
    <div class="url">http://fieldnote.net/4xPq7Lm</div>
  </div>
  <div class="abs col" style="left:630px;top:18px">
    <h4>Follow us</h4>
    <div class="follow">
      <span class="sq-blue" role="img" aria-label="Social page"></span>
      <span class="sq-teal" role="img" aria-label="Social feed"></span>
      <span class="sq-li" role="img" aria-label="Professional network"></span>
      <span class="sq-or" role="img" aria-label="Blog"></span>
    </div>
  </div>
  <div class="abs copy">© 2014.www.halvardtraining.com</div>
  <div class="abs code">M1</div>
</footer>

</body>
</html>
```